FSA Expiring Soon 2023

Hi,
Looking to upgrade the design of current flyer to be used as an e-blast.
-8.5"x11"
-Under 5MB
-Several formats, PDF, .ai, jpeg, png

This flyer should be simple, yet eye catching. The goal is to remind patients that their Flexible Spending Account (FSA) will be expiring soon and that they can use their FSA or HSA to purchase most of our over the counter items, including inserts and shoes.

-must include: Some insurance plans require a letter of medical necessity
-must include: Each flexible spending account varies on their expiration date
- stock images must be free

I'll attach our logo and old flyer as well for reference.

Thank you,
Oscar

```html
<!DOCTYPE html>
<html lang="en">
<head>
<meta charset="utf-8">
<title>FSA Expiring Soon</title>
<link href="https://fonts.googleapis.com/css2?family=Poppins:wght@400;500;600;700&display=swap" rel="stylesheet">
<style>
:root{
  --orange:#ff7c4a;
  --ink:#454545;
  --text:#4b4b4b;
  --paper:#ffffff;
  --stage:#2d2d2d;
  --wood:#d8c09a;
  --desk:#ececec;
}
*{margin:0;padding:0;box-sizing:border-box}
html,body{width:1200px;height:1200px;overflow:hidden;background:var(--stage);font-family:'Poppins',sans-serif}
.flyer{position:absolute;left:136px;top:0;width:927px;height:1200px;background:var(--paper);overflow:hidden}
.hero-top{position:absolute;left:0;top:0;width:927px;height:110px;background:linear-gradient(180deg,#e6e6e6,#e9e9e9)}
.hero-photo{position:absolute;left:0;top:110px;width:927px;height:470px;
  background:
    radial-gradient(ellipse 230px 110px at 515px 205px,var(--wood) 0%,rgba(216,192,154,.75) 55%,rgba(216,192,154,0) 100%),
    radial-gradient(ellipse 420px 140px at 520px 300px,#f7f7f7 0%,rgba(247,247,247,0) 100%),
    linear-gradient(180deg,#e9e9e9 0%,#eeeeee 45%,#f6f6f6 75%,#ffffff 100%)}
.brand{position:absolute;left:35px;top:40px;display:flex;align-items:center;gap:10px}
.brand-mark{width:18px;height:18px;background:var(--orange)}
.brand-name{color:var(--orange);font-weight:600;font-size:24px;line-height:1}
.contact{position:absolute;right:35px;top:22px;text-align:right}
.contact-web{color:var(--ink);font-size:17px;font-weight:500}
.contact-phone{display:flex;align-items:center;justify-content:flex-end;gap:6px;color:var(--ink);font-size:28px;font-weight:700;margin-top:6px}
.headline{position:absolute;left:0;width:100%;top:532px;text-align:center;font-weight:600;font-size:120px;letter-spacing:-2px;line-height:1.1}
.headline .accent{color:var(--orange)}
.headline .dark{color:var(--ink)}
.lead{position:absolute;left:0;width:100%;text-align:center;color:var(--text);font-size:30px;line-height:43px}
.lead-one{top:686px}
.lead-two{top:790px}
.divider{position:absolute;left:239px;top:888px;width:458px;height:2px;background:var(--ink)}
.notes{position:absolute;left:0;width:100%;top:899px;text-align:center;color:var(--orange);font-size:24px;line-height:40px}
.footer-band{position:absolute;left:0;top:1023px;width:927px;height:177px;background:var(--orange);border-radius:60px 60px 0 0}
.cta{position:absolute;left:161px;top:993px;width:604px;height:56px;background:var(--paper);border:2px solid var(--orange);border-radius:30px;
  display:flex;align-items:center;justify-content:center;color:var(--ink);font-weight:600;font-size:43px;letter-spacing:-0.5px;line-height:1}
.offices{position:absolute;left:35px;right:35px;top:1062px;display:flex;justify-content:space-between;color:#fff}
.office{width:267px;font-size:17px;line-height:30px}
.office h3{font-size:21px;font-weight:600;line-height:30px;margin-bottom:4px}
.office-left{text-align:left}
.office-center{text-align:center}
.office-right{text-align:right}
.office-rule{position:absolute;top:1088px;width:2px;height:78px;background:#fff}
</style>
</head>
<body>
<main class="flyer">
  <div class="hero-top"></div>
  <div class="hero-photo" role="img" aria-label="Photo of wooden blocks spelling FSA on a white keyboard beside glasses, a plant and a notebook"></div>

  <div class="brand">
    <span class="brand-mark"></span>
    <span class="brand-name">Riverton Foot &amp; Ankle</span>
  </div>

  <div class="contact">
    <div class="contact-web">www.stridewellfeet.com</div>
    <div class="contact-phone">
      <svg width="26" height="26" viewBox="0 0 24 24" aria-hidden="true"><path fill="#ff7c4a" d="M6.6 10.8a15.1 15.1 0 0 0 6.6 6.6l2.2-2.2a1 1 0 0 1 1-.25 11.4 11.4 0 0 0 3.6.57 1 1 0 0 1 1 1V20a1 1 0 0 1-1 1A17 17 0 0 1 3 4a1 1 0 0 1 1-1h3.5a1 1 0 0 1 1 1c0 1.25.2 2.45.57 3.57a1 1 0 0 1-.25 1z"/><path fill="none" stroke="#ff7c4a" stroke-width="1.6" stroke-linecap="round" d="M14 3a7 7 0 0 1 7 7M14 6.5a3.5 3.5 0 0 1 3.5 3.5"/></svg>
      <span>(877)555-0142</span>
    </div>
  </div>

  <h1 class="headline"><span class="accent">Expiring</span> <span class="dark">Soon!</span></h1>

  <p class="lead lead-one">Use your Flexible Spending Account Funds(FSA) before<br>they expire at the end of the year.</p>
  <p class="lead lead-two">You can use your FSA or HSA to purchase most of our<br>over the counter items, including inserts and shoes.</p>

  <div class="divider"></div>

  <p class="notes">Some insurance plans require a letter of medical necessity.<br>Each flexible spending account varies on their expiration date.</p>

  <div class="footer-band"></div>
  <div class="cta">Request an appointment</div>

  <div class="office-rule" style="left:302px"></div>
  <div class="office-rule" style="left:629px"></div>

  <section class="offices">
    <div class="office office-left">
      <h3>Riverton Office</h3>
      210 Maple Grove Dr.<br>Ste. 140<br>Riverton, MD 21790
    </div>
    <div class="office office-center">
      <h3>Lakeview Office</h3>
      2875 Harbor Pointe Blvd.<br>Ste. 305<br>Lakeview, MD 21795
    </div>
    <div class="office office-right">
      <h3>Ashford Office</h3>
      88 Wellness Way<br>Ashford,<br>WV&nbsp; 25499
    </div>
  </section>
</main>
</body>
</html>
```